Brindlewood Business Card Design

Small Company
looking to ramp up work need business cards sick of everyone asking for a card
client base is broad.
keep it simple
Just want on the reverse of the card somewhere for me to write details for clients
appointments etc..
want to use the phrase
"Your safe, reliable and trust worthy Tradesmen"

Industry/Entity Type

Business

Contact Information for Business Card

Brindlewood Electrical Solutions Pty Ltd
Director Gregory Brindlewood
email - brindlewoodelectricalsolutions@zentromail.net
Ph - 03 95418276
Mobile - 0417592836
Domestic, Industrial, Commercial & Mining
Electrical, Solar, Communications & Fibre
REC: 41873

```html
<!DOCTYPE html>
<html lang="en">
<head>
<meta charset="utf-8">
<title>Brindlewood Electrical Solutions – Business Card</title>
<link rel="stylesheet" href="https://fonts.googleapis.com/css2?family=Open+Sans:wght@400&family=PT+Sans:ital,wght@0,400;0,700;1,400&display=swap">
<style>
  :root {
    --navy: #2a3590;
    --red: #ec1c24;
    --white: #ffffff;
    --backdrop: #8c8c8c;
    --card-shadow: rgba(0,0,0,0.25);
  }
  * { box-sizing: border-box; margin: 0; padding: 0; }
  html, body { width: 1200px; height: 1000px; overflow: hidden; }
  body { background: var(--backdrop); position: relative; font-family: "PT Sans", sans-serif; }

  .card {
    position: absolute;
    width: 686px;
    height: 435px;
    background: var(--white);
    box-shadow: 2px 3px 6px var(--card-shadow);
    overflow: hidden;
  }
  .card--front { left: 36px; top: 30px; }
  .card--back { left: 463px; top: 520px; }

  .brand {
    position: absolute;
    left: 0; right: 0; top: 28px;
    text-align: center;
    color: var(--navy);
    font-family: "Open Sans", sans-serif;
    font-weight: 400;
    line-height: 1;
  }
  .brand__dot {
    display: block;
    width: 18px; height: 18px;
    margin: 0 auto 8px;
    border-radius: 50%;
    background: var(--red);
  }
  .brand__name { display: block; font-size: 62px; letter-spacing: -1px; }
  .brand__sub { display: block; font-size: 24px; margin-top: 6px; letter-spacing: 0.5px; }

  .tagline-band {
    position: absolute;
    left: 0; right: 0; top: 170px; height: 28px;
    background: var(--red);
    color: var(--white);
    font-style: italic;
    font-size: 18px;
    line-height: 28px;
    text-align: center;
    padding-left: 30px;
  }

  .services-band {
    position: absolute;
    left: 0; right: 0; bottom: 0; height: 22px;
    background: var(--navy);
    color: var(--white);
    font-style: italic;
    font-size: 14.5px;
    line-height: 22px;
    text-align: center;
    white-space: nowrap;
  }

  .person {
    position: absolute;
    left: 22px; top: 278px;
    color: var(--navy);
    font-weight: 700;
    font-size: 23px;
    line-height: 25px;
  }
  .divider {
    position: absolute;
    left: 262px; top: 260px;
    width: 2px; height: 88px;
    background: var(--red);
  }
  .contacts {
    position: absolute;
    left: 272px; top: 259px;
    list-style: none;
    color: var(--navy);
    font-weight: 700;
    font-size: 19px;
    white-space: nowrap;
  }
  .contacts li { display: flex; align-items: center; height: 31.5px; }
  .contacts .contacts__email { font-size: 15px; letter-spacing: -0.1px; }
  .contacts svg { width: 24px; height: 24px; margin-right: 3px; flex: none; }

  .appointment {
    position: absolute;
    left: 0; top: 228px; width: 660px;
    text-align: center;
    color: var(--navy);
    font-weight: 700;
    font-size: 27px;
  }
  .fields { position: absolute; left: 163px; top: 284px; }
  .field { display: flex; align-items: center; height: 37.5px; }
  .field__label { width: 76px; color: var(--red); font-weight: 700; font-size: 20px; }
  .field__line { width: 244px; border-bottom: 2px dashed var(--navy); margin-top: 10px; }
</style>
</head>
<body>

<section class="card card--front" aria-label="Business card front">
  <div class="brand">
    <span class="brand__dot"></span>
    <span class="brand__name">Brindlewood</span>
    <span class="brand__sub">ELECTRICAL SOLUTIONS</span>
  </div>
  <div class="tagline-band">"Your safe, reliable and trust worthy Tradesmen"</div>

  <div class="person">Gregory Brindlewood<br>Director</div>
  <div class="divider"></div>
  <ul class="contacts">
    <li>
      <svg viewBox="0 0 24 24" aria-hidden="true"><circle cx="12" cy="12" r="12" fill="var(--red)"/><rect x="8.5" y="4.5" width="7" height="15" rx="1.2" fill="none" stroke="#fff" stroke-width="1.6"/><rect x="10" y="7" width="4" height="5" fill="#fff"/></svg>
      0417592836
    </li>
    <li>
      <svg viewBox="0 0 24 24" aria-hidden="true"><circle cx="12" cy="12" r="12" fill="var(--red)"/><path d="M7.5 6.5c1-.8 2-.6 2.5.3l1 1.8c.4.8.1 1.4-.6 1.9-.4.3-.4.7-.1 1.3.8 1.4 1.8 2.4 3.1 3.1.6.3 1 .3 1.3-.1.5-.7 1.1-1 1.9-.6l1.8 1c.9.5 1.1 1.5.3 2.5-1.2 1.4-3 1.5-5 .4-2.6-1.4-4.8-3.6-6.2-6.2-1.1-2-1-3.8.4-5z" fill="#fff"/></svg>
      03 95418276
    </li>
    <li class="contacts__email">
      <svg viewBox="0 0 24 24" aria-hidden="true"><circle cx="12" cy="12" r="12" fill="var(--red)"/><rect x="5.5" y="7.5" width="13" height="9" fill="#fff"/><path d="M5.5 7.5l6.5 5 6.5-5" fill="none" stroke="var(--red)" stroke-width="1.2"/></svg>
      brindlewoodelectricalsolutions@zentromail.net
    </li>
  </ul>

  <div class="services-band">Domestic, Industrial, Commercial &amp; Mining Electrical, Solar, Communications &amp; Fibre REC: 41873</div>
</section>

<section class="card card--back" aria-label="Business card back">
  <div class="brand">
    <span class="brand__dot"></span>
    <span class="brand__name">Brindlewood</span>
    <span class="brand__sub">ELECTRICAL SOLUTIONS</span>
  </div>
  <div class="tagline-band">"Your safe, reliable and trust worthy Tradesmen"</div>

  <h2 class="appointment">Appointment</h2>
  <div class="fields">
    <div class="field"><span class="field__label">Name:</span><span class="field__line"></span></div>
    <div class="field"><span class="field__label">Date:</span><span class="field__line"></span></div>
    <div class="field"><span class="field__label">Time:</span><span class="field__line"></span></div>
  </div>

  <div class="services-band">Domestic, Industrial, Commercial &amp; Mining Electrical, Solar, Communications &amp; Fibre REC: 41873</div>
</section>

</body>
</html>
```